Post Card Design - Photo on front, details on back. Logo on both sides.

Back: See the photo of my old card. The back worked well, as it gave me lots of space to write on. The address details are still correct, but the logo has changed to Josephine Sans. Logo can be on one line or on two (if two, align it on the left).
Don't include the 'BEAUTIFUL WEDDING DRESSES...' bit.
I'd like to print this on thicker, slightly coarse paper, so don't go too small on detail.
Here are the Quorl paper details: Paper Stock: Natural Uncoated
Paper Thickness: Premium
Finish: None
Front of Card: I'd like to see options for both pictures:
I think the painted image would look best with a frame in a pale shade and the logo in the frame fairly subtle.
The actual dress photo I'd like to see cropped a bit like in my mock up. You'll need to have a look at how the logo would be best placed on this. You can place it anywhere, or add a banner.
See my website for my brand's look: lorabetwick.co.nz
Target Market(s)
Brides
Industry/Entity Type
Wedding Dresses
Contact Information for Business Card
Front: Photo and logo. Back: with details and lots of empty space. See attached photos for loose brief.
Other font styles liked:
- Josephine Sans
Requirements
Must have
- I hand-write the gown designs and price on the back of the card, so there needs to be plenty of empty space.
Nice to have
- As per brief.
Should not have
- It must look clean, romantic, modern. Timeless.

```html
<!DOCTYPE html>
<html lang="en">
<head>
<meta charset="utf-8">
<title>Lora Betwick – Post Card</title>
<link href="https://fonts.googleapis.com/css2?family=Josefin+Sans:wght@300;400&display=swap" rel="stylesheet">
<style>
  :root {
    --board: #424140;
    --card-gold: #dcc08a;
    --frame-pale: #e2cc9c;
    --band-gold: #e0c998;
    --paper: #ffffff;
    --ink: #1c1a17;
    --art-cream: #f3dfb0;
    --art-pink: #eea7a0;
    --art-rose: #e98a8a;
  }
  * { margin: 0; padding: 0; box-sizing: border-box; }
  html, body {
    width: 1200px; height: 1200px; overflow: hidden;
    background: var(--board);
    font-family: "Josefin Sans", sans-serif;
    color: var(--ink);
  }
  .canvas { position: relative; width: 1200px; height: 1200px; }
  .card {
    position: absolute; left: 156px; width: 889px;
    box-shadow: 0 4px 14px rgba(0,0,0,.35);
    overflow: hidden;
  }
  .card--front { top: 38px; height: 550px; background: var(--card-gold); }
  .card--back { top: 612px; height: 550px; background: var(--paper); }

  .front-frame {
    position: absolute; left: 241px; top: 30px; width: 407px; height: 490px;
    background: var(--frame-pale);
  }
  .front-art {
    position: absolute; left: 27px; top: 26px; width: 354px; height: 436px;
    background:
      radial-gradient(ellipse at 40% 62%, var(--art-rose) 0%, var(--art-pink) 28%, transparent 58%),
      radial-gradient(ellipse at 70% 45%, #f6ead3 0%, transparent 45%),
      linear-gradient(180deg, var(--art-cream), #f1d8a8);
  }
  .front-name {
    position: absolute; left: 0; right: 0; top: 490px;
    text-align: center; font-weight: 300; font-size: 35px; letter-spacing: 1px;
    line-height: 1;
  }

  .back-name {
    position: absolute; left: 46px; top: 52px;
    font-weight: 300; font-size: 35px; letter-spacing: 1px; line-height: 1;
  }
  .contact { position: absolute; left: 48px; top: 406px; }
  .contact-rail {
    position: absolute; left: 0; top: 0; width: 23px; height: 94px;
    background: var(--band-gold); border-radius: 4px;
  }
  .contact-row {
    position: absolute; left: 0; display: flex; align-items: center;
    white-space: nowrap; font-weight: 300; line-height: 1;
  }
  .contact-row svg { width: 23px; height: 16px; flex: none; }
  .contact-row span { margin-left: 6px; }
  .row-phone { top: 2px; font-size: 22px; }
  .row-email { top: 34px; font-size: 19px; }
  .row-web { top: 68px; font-size: 24px; }
  .back-band {
    position: absolute; left: 0; bottom: 0; width: 100%; height: 32px;
    background: var(--band-gold);
  }
</style>
</head>
<body>
<div class="canvas">
  <section class="card card--front">
    <div class="front-frame">
      <div class="front-art" role="img" aria-label="Painted vintage illustration of a couple surrounded by pink and peach flowers"></div>
      <div class="front-name">LORA BETWICK</div>
    </div>
  </section>

  <section class="card card--back">
    <div class="back-name">LORA BETWICK</div>
    <div class="contact">
      <div class="contact-rail"></div>
      <div class="contact-row row-phone">
        <svg viewBox="0 0 23 16"><path d="M8 2.5c.8-.5 1.5-.3 2 .6l.9 1.6c.3.6.2 1.1-.3 1.5l-.8.6c.5 1.3 1.4 2.3 2.6 3l.7-.8c.4-.5 1-.6 1.5-.2l1.5 1c.7.5.8 1.2.3 1.9-.8 1-2 1.5-3.3.9C9.5 11.4 7.6 9.2 6.9 6.4 6.6 4.8 7 3.3 8 2.5z" fill="var(--ink)"/></svg>
        <span>+64 352 0947</span>
      </div>
      <div class="contact-row row-email">
        <svg viewBox="0 0 23 16"><rect x="5" y="3.5" width="13" height="9" fill="none" stroke="var(--ink)" stroke-width="1.4"/><path d="M5 3.5l6.5 5 6.5-5M5 12.5l4.5-4M18 12.5l-4.5-4" fill="none" stroke="var(--ink)" stroke-width="1.2"/></svg>
        <span>lora@lorabetwick.co.nz</span>
      </div>
      <div class="contact-row row-web">
        <svg viewBox="0 0 23 16"><circle cx="11.5" cy="8" r="6.5" fill="none" stroke="var(--ink)" stroke-width="1.6"/><ellipse cx="11.5" cy="8" rx="2.8" ry="6.5" fill="none" stroke="var(--ink)" stroke-width="1.3"/><path d="M5 8h13M6 4.8h11M6 11.2h11" stroke="var(--ink)" stroke-width="1.2"/></svg>
        <span>LORABETWICK.CO.NZ</span>
      </div>
    </div>
    <div class="back-band"></div>
  </section>
</div>
</body>
</html>
```